A4 Flyer Design outlining our financial philosophy

One A4 page design (landscape orientation) outlining our financial philosophy.
The design needs to show these steps as the building blocks and the path taken to financial success:
1. Maximise income and reduce expenses
2. Maximise savings and reduce bad debts
3. Invest wisely & tax effectively
4. Manage risk
5. Plan for retirement
6. Leave a legacy
The design needs to incorporate the 6 building blocks above along with the key points for each topic. More info attached.
Design must be engaging, professional and consistent with our current branding colours.

Target Market(s)

self employed individuals looking to build wealth through property and shares.

Industry/Entity Type

Financial Planning

Font styles to use
Sans Serif

Colors
0255a3
5c5c5c
000000
ffffff

Requirements
Must have
• clear and engaging.
• consistent with current branding
• 6 topics with key considerations (as per attached)
• must show that all 6 points are linked and are a journey.

```html
<!DOCTYPE html>
<html lang="en">
<head>
<meta charset="utf-8">
<title>Kinward Financial Group – Building Blocks to Financial Success</title>
<link href="https://fonts.googleapis.com/css2?family=Lato:wght@700&family=Montserrat:wght@400&display=swap" rel="stylesheet">
<style>
  :root {
    --brand-blue: #0255a3;
    --text-grey: #5c5c5c;
    --ink: #000000;
    --white: #ffffff;
    --panel-grey: #d9d9d9;
    --url-ink: #1d2c4a;
  }
  * { margin: 0; padding: 0; box-sizing: border-box; }
  html, body { width: 1200px; height: 848px; overflow: hidden; background: var(--panel-grey); }
  .flyer { position: relative; width: 1200px; height: 848px; background: var(--panel-grey); font-family: "Montserrat", Arial, sans-serif; color: var(--ink); }

  .hero-photo {
    position: absolute; left: 0; top: 16px; width: 1200px; height: 289px;
    background: linear-gradient(100deg, #e6e4e1 0%, #d8d4cf 30%, #3a3f4e 55%, #2a2f3c 70%, #c9d3e4 88%, #eef1f6 100%);
  }

  .brand-box {
    position: absolute; left: 43px; top: 51px; width: 359px; height: 138px;
    background: var(--white); display: flex; align-items: center; gap: 18px; padding-left: 24px;
  }
  .brand-dot { width: 86px; height: 86px; border-radius: 50%; background: var(--brand-blue); flex: none; }
  .brand-name {
    font-family: "Lato", Arial, sans-serif; font-weight: 700; color: var(--brand-blue);
    font-size: 27px; line-height: 1.15; letter-spacing: 1px;
  }

  .step-title {
    position: absolute; background: var(--white); display: flex; align-items: center; justify-content: center;
    text-align: center; font-family: "Lato", Arial, sans-serif; font-weight: 700; color: var(--text-grey);
    font-size: 20px; line-height: 1.35; text-transform: uppercase;
  }
  .step-points { position: absolute; list-style: none; font-size: 14px; line-height: 18.5px; color: var(--ink); }
  .step-points.lower { font-size: 15px; line-height: 22.5px; }
  .step-points li { position: relative; padding-left: 13px; }
  .step-points li::before {
    content: ""; position: absolute; left: 0; top: 6px; width: 8px; height: 8px; border-radius: 50%; background: var(--brand-blue);
  }
  .step-points.lower li::before { top: 8px; }

  .journey-path { position: absolute; left: 0; top: 0; width: 1200px; height: 848px; pointer-events: none; }

  .closing-band {
    position: absolute; left: 0; top: 758px; width: 1200px; height: 73px; background: var(--brand-blue);
    text-align: center;
  }
  .closing-line { color: var(--white); font-size: 24px; padding-top: 16px; }
  .closing-url { color: var(--url-ink); font-size: 13px; margin-top: 6px; }
</style>
</head>
<body>
<div class="flyer">
  <div class="hero-photo" role="img" aria-label="Photo of a business person reviewing financial charts on a tablet"></div>

  <div class="brand-box">
    <span class="brand-dot"></span>
    <span class="brand-name">KINWARD<br>FINANCIAL GROUP</span>
  </div>

  <!-- Row one -->
  <div class="step-title" style="left:56px;top:328px;width:256px;height:90px;">Maximise income and<br>reduce expenses</div>
  <ul class="step-points" style="left:46px;top:434px;width:380px;">
    <li>Invest in yourself through education and training</li>
    <li>Build a number of income streams</li>
    <li>Align you're spending with your values</li>
    <li>Track your spending</li>
    <li>Increase surplus income</li>
  </ul>

  <div class="step-title" style="left:473px;top:328px;width:257px;height:90px;">Maximise savings<br>and reduce<br>bad debts</div>
  <ul class="step-points" style="left:463px;top:434px;width:330px;">
    <li>Surplus income increases savings</li>
    <li>You savings and equity for investment</li>
    <li>Avoid borrowing for lifestyle assets /<br>experiences where possible</li>
  </ul>

  <div class="step-title" style="left:882px;top:328px;width:258px;height:90px;">Invest wisely &amp;<br>tax effectively</div>
  <ul class="step-points" style="left:885px;top:434px;width:315px;">
    <li>Build an investment portfolio e.g.<br>property and shares</li>
    <li>Use appropriate tax structures such as</li>
    <li>Family Trusts / Superannuation</li>
    <li>Depreciation schedules</li>
  </ul>

  <!-- Row two -->
  <div class="step-title" style="left:56px;top:543px;width:256px;height:94px;">Manage risk</div>
  <ul class="step-points lower" style="left:46px;top:649px;width:300px;">
    <li>Insurance in various forms</li>
    <li>Contingency plans</li>
    <li>Diversification</li>
    <li>Focus on quality</li>
  </ul>

  <div class="step-title" style="left:473px;top:543px;width:257px;height:90px;">Plan for<br>retirement</div>
  <ul class="step-points" style="left:463px;top:644px;width:380px;font-size:14px;line-height:19.5px;">
    <li>Replacement of your salary or profits from<br>running a business with income from your<br>investment portfolio</li>
    <li>Drawing a sustainable income to maintain a great<br>lifestyle and protect your retirement nest egg</li>
  </ul>

  <div class="step-title" style="left:891px;top:543px;width:257px;height:87px;">Leave a legacy</div>
  <ul class="step-points lower" style="left:885px;top:649px;width:300px;">
    <li>Having a Will</li>
    <li>Power of Attorney</li>
    <li>Testamentary Trust?</li>
  </ul>

  <svg class="journey-path" viewBox="0 0 1200 848" aria-hidden="true">
    <g fill="none" stroke="var(--brand-blue)" stroke-width="3.5">
      <polyline points="289,330 368,330 368,397 487,397"/>
      <polyline points="704,406 914,406"/>
      <polyline points="876,356 876,460 820,460 820,533 334,533 285,581"/>
      <polyline points="278,612 487,612"/>
      <polyline points="695,554 791,554 791,613 898,613"/>
    </g>
    <g fill="var(--brand-blue)">
      <circle cx="487" cy="397" r="11"/>
      <circle cx="914" cy="406" r="11"/>
      <circle cx="876" cy="356" r="10"/>
      <circle cx="285" cy="581" r="11"/>
      <circle cx="487" cy="612" r="11"/>
      <circle cx="898" cy="613" r="10"/>
    </g>
  </svg>

  <div class="closing-band">
    <p class="closing-line">Achieve long lasting Financial Success. Start Today.</p>
    <p class="closing-url">www.kinwardfg.com.au</p>
  </div>
</div>
</body>
</html>
```